Carpet cleaning company focused on high quality needs business cards

We are a growing company that just merged with another company and need to design a new business card. We do both residential as well as commercial cleaning. We do carpet, tile & grout, upholstery, hard floors, and stain & pet odor removal. We treat our customers like family and strive to achieve outstanding results with every job.

```html
<!DOCTYPE html>
<html lang="en">
<head>
<meta charset="utf-8">
<title>Harlow's Carpet Crew – Business Card</title>
<link rel="stylesheet" href="https://fonts.googleapis.com/css2?family=Lato:ital,wght@0,400;0,700;0,900;1,400&display=swap">
<style>
  :root {
    --backdrop: #2b2e33;
    --card: #f3e5cb;
    --ink: #1f1f1f;
    --red: #ec4641;
    --red-deep: #d83a36;
    --blue: #1a7cc4;
    --muted: #3a3a3a;
  }
  * { box-sizing: border-box; margin: 0; padding: 0; }
  html, body {
    width: 1200px; height: 952px; overflow: hidden;
    background: var(--backdrop);
    font-family: "Lato", Arial, sans-serif;
  }
  .sheet {
    position: relative; width: 1200px; height: 952px;
  }
  .card {
    position: absolute;
    width: 525px; height: 300px;
    background: var(--card);
    border-radius: 26px;
    overflow: hidden;
    box-shadow: 0 18px 40px rgba(0,0,0,.45);
  }
  /* Front: logo side */
  .card--front { left: 50px; top: 490px; }
  .logo {
    position: absolute; left: 70px; top: 62px;
    display: flex; align-items: flex-end; gap: 22px;
  }
  .logo__mascot {
    width: 150px; height: 150px;
    background: linear-gradient(135deg, #f0544e 0%, var(--red-deep) 100%);
  }
  .logo__name {
    font-weight: 900; color: var(--ink);
    font-size: 34px; line-height: 1.02; letter-spacing: .5px;
    text-transform: uppercase;
    padding-bottom: 4px;
  }
  /* Back: contact side */
  .card--back { left: 625px; top: 150px; }
  .holder { position: absolute; left: 34px; top: 32px; }
  .holder__name {
    font-weight: 900; font-size: 22px; letter-spacing: 1px;
    text-transform: uppercase;
  }
  .holder__first { color: var(--red); font-weight: 400; }
  .holder__last { color: var(--blue); }
  .holder__role {
    font-style: italic; font-size: 13px; color: var(--muted); margin-top: 2px;
  }
  .holder__rule {
    width: 44px; height: 2px; background: var(--ink); margin-top: 8px;
  }
  .contact {
    position: absolute; left: 34px; top: 126px;
    list-style: none; font-size: 12.5px; color: var(--ink); line-height: 1.35;
  }
  .contact li { display: flex; align-items: flex-start; gap: 9px; margin-bottom: 7px; }
  .contact__icon {
    flex: none; width: 17px; height: 17px; border-radius: 3px;
    display: flex; align-items: center; justify-content: center;
    background: var(--red);
  }
  .contact__icon--blue { background: var(--blue); }
  .contact__icon svg { width: 11px; height: 11px; fill: #fff; }
  .mascot-panel {
    position: absolute; right: 0; bottom: 0;
    width: 250px; height: 190px;
    border-top-left-radius: 70px;
    background: linear-gradient(160deg, #f0504a 0%, var(--red-deep) 100%);
  }
</style>
</head>
<body>
<main class="sheet">

  <section class="card card--front" aria-label="Card front">
    <div class="logo">
      <div class="logo__mascot" role="img" aria-label="Mascot illustration: cheerful cleaner in a blue cap raising a carpet-cleaning wand on a red square"></div>
      <div class="logo__name">Harlow's<br>Carpet Crew</div>
    </div>
  </section>

  <section class="card card--back" aria-label="Card back">
    <div class="holder">
      <h1 class="holder__name"><span class="holder__first">Mira J.</span> <span class="holder__last">Okafor</span></h1>
      <p class="holder__role">Managing Director</p>
      <div class="holder__rule"></div>
    </div>

    <ul class="contact">
      <li>
        <span class="contact__icon contact__icon--blue">
          <svg viewBox="0 0 24 24"><path d="M12 2a7 7 0 0 0-7 7c0 5 7 13 7 13s7-8 7-13a7 7 0 0 0-7-7zm0 9.5A2.5 2.5 0 1 1 12 6a2.5 2.5 0 0 1 0 5.5z"/></svg>
        </span>
        <span>218 Linden Park Road<br>Fairbrook, OH 44012</span>
      </li>
      <li>
        <span class="contact__icon">
          <svg viewBox="0 0 24 24"><path d="M6.6 10.8a15 15 0 0 0 6.6 6.6l2.2-2.2c.3-.3.7-.4 1-.2 1.1.4 2.3.6 3.6.6.6 0 1 .4 1 1V20c0 .6-.4 1-1 1A17 17 0 0 1 3 4c0-.6.4-1 1-1h3.5c.6 0 1 .4 1 1 0 1.3.2 2.5.6 3.6.1.3 0 .7-.2 1z"/></svg>
        </span>
        <span>+00 555 210 47</span>
      </li>
      <li>
        <span class="contact__icon">
          <svg viewBox="0 0 24 24"><path d="M3 5h18v14H3z M4.5 6.5 12 12l7.5-5.5v-.1H4.5z" fill-rule="evenodd"/></svg>
        </span>
        <span>hello@harlowscarpet.com</span>
      </li>
      <li>
        <span class="contact__icon">
          <svg viewBox="0 0 24 24"><path d="M12 2a10 10 0 1 0 0 20 10 10 0 0 0 0-20zm6.9 9h-3a15 15 0 0 0-1.3-5.6A8 8 0 0 1 18.9 11zM12 4.1c.9 1.2 1.7 3.6 1.9 6.9h-3.8c.2-3.3 1-5.7 1.9-6.9zM9.4 5.4A15 15 0 0 0 8.1 11h-3a8 8 0 0 1 4.3-5.6zM5.1 13h3a15 15 0 0 0 1.3 5.6A8 8 0 0 1 5.1 13zm6.9 6.9c-.9-1.2-1.7-3.6-1.9-6.9h3.8c-.2 3.3-1 5.7-1.9 6.9zm2.6-1.3a15 15 0 0 0 1.3-5.6h3a8 8 0 0 1-4.3 5.6z"/></svg>
        </span>
        <span>www.harlowscarpet.com</span>
      </li>
    </ul>

    <div class="mascot-panel" role="img" aria-label="Mascot illustration: cleaner in blue shirt and cap lifting a carpet-cleaning wand with hose"></div>
  </section>

</main>
</body>
</html>
```